Sparkling Wine Label

Need a new label design for my new product being launched. We are a wine company based in Los Angeles CA that currently produces two labels that were design on Pixel Harbor. Please review the attached file "Sparkling Label Design" which will have all details needed to complete. If not, please feel free to reach out by email.

Target Market(s)

Adults

Industry/Entity Type

It Company

Font styles to use
Script

Colors
8869ae
ffffff

Requirements
Must have
• Government Warning
• www.dorvanelwineco.com
• signature on back
• Script for the brand title: Velisse
Nice to have
• very elegant design.

```html
<!DOCTYPE html>
<html lang="en">
<head>
<meta charset="utf-8">
<title>Dorvanel Wine Company | Velisse – Sparkling Riesling Label Concept</title>
<link rel="stylesheet" href="https://fonts.googleapis.com/css2?family=Cinzel:wght@400;600&family=Great+Vibes&family=Roboto+Condensed:wght@400;700&display=swap">
<style>
  :root {
    --board: #000000;
    --footer: #222222;
    --turquoise: #17b2b6;
    --turquoise-swatch: #1fe0e8;
    --ink: #0b3537;
    --foil-flat: #cfd4d6;
    --foil-line: #e4e8e9;
    --heading: #ffffff;
    --caption: #bfbfbf;
    --foil: linear-gradient(135deg, #8b8b8b 0%, #f3f3f3 28%, #9c9c9c 52%, #ececec 78%, #7e7e7e 100%);
  }
  * { box-sizing: border-box; margin: 0; padding: 0; }
  html, body { width: 1200px; height: 882px; overflow: hidden; }
  body {
    position: relative;
    background: var(--board);
    font-family: "Roboto Condensed", "Arial Narrow", sans-serif;
    color: var(--heading);
  }

  /* Board heading */
  .board-title {
    position: absolute; left: 41px; top: 32px;
    font-size: 32px; font-weight: 700; letter-spacing: -0.2px;
    display: flex; align-items: center;
  }
  .board-title .divider {
    display: inline-block; width: 2px; height: 38px;
    background: var(--heading); margin: 0 12px;
  }
  .board-subtitle {
    position: absolute; left: 41px; top: 80px;
    font-size: 22px; font-weight: 400;
  }
  .view-caption {
    position: absolute; top: 230px;
    font-size: 23px; color: var(--caption);
  }

  /* Label frame */
  .label {
    position: absolute; top: 279px; height: 368px;
    background: var(--foil);
    padding: 11px;
  }
  .label-band {
    width: 100%; height: 100%;
    background: var(--turquoise);
    padding: 5px;
  }
  .label-rule {
    width: 100%; height: 100%;
    border: 2px solid var(--foil-line);
    padding: 5px;
  }
  .label-panel {
    position: relative;
    width: 100%; height: 100%;
    border: 1px solid var(--ink);
    text-align: center;
    color: var(--ink);
  }

  .brand-dot {
    display: block; margin: 0 auto;
    border-radius: 50%; background: var(--foil-flat);
  }
  .brand-name {
    font-family: "Great Vibes", cursive;
    color: var(--foil-flat);
    font-weight: 400;
    line-height: 1;
  }
  .varietal {
    font-family: "Cinzel", serif;
    font-weight: 600;
    color: var(--ink);
    line-height: 1;
  }

  /* Front */
  .label-front { left: 76px; width: 612px; }
  .label-front .brand-dot { width: 16px; height: 16px; margin-top: 38px; }
  .label-front .brand-name { font-size: 138px; margin-top: 6px; }
  .label-front .varietal { font-size: 34px; letter-spacing: 1.5px; margin-top: 4px; }
  .label-front .spec {
    position: absolute; bottom: 18px;
    font-size: 16px; color: var(--ink);
  }
  .label-front .spec-volume { left: 28px; }
  .label-front .spec-abv { right: 28px; }

  /* Back */
  .label-back { left: 750px; width: 369px; padding: 7px; }
  .label-back .label-band { padding: 4px; }
  .label-back .label-rule { padding: 4px; }
  .label-back .brand-dot { width: 11px; height: 11px; margin-top: 20px; }
  .label-back .brand-name { font-size: 78px; margin-top: 2px; }
  .label-back .varietal { font-size: 21px; letter-spacing: 1px; margin-top: 0; }
  .origin {
    display: inline-block; margin-top: 5px; padding-top: 2px;
    border-top: 1px solid var(--foil-line);
    font-family: "Cinzel", serif; font-size: 13px; letter-spacing: 1px;
    color: var(--foil-flat); width: 170px;
  }
  .website { margin-top: 14px; font-size: 13px; font-weight: 700; }
  .warning {
    margin: 10px auto 0; width: 300px;
    font-size: 9.6px; font-weight: 700; line-height: 1.3;
    text-transform: uppercase;
  }
  .back-specs {
    display: flex; justify-content: space-between;
    margin: 20px 20px 0; font-size: 11px;
  }
  .bottler { margin-top: 9px; font-size: 7.4px; font-weight: 700; }

  /* Colour legend */
  .legend {
    position: absolute; left: 81px; top: 762px;
    display: flex; align-items: center; font-size: 21px;
  }
  .swatch { width: 32px; height: 32px; margin-right: 12px; }
  .swatch-turquoise { background: var(--turquoise-swatch); }
  .swatch-foil { background: linear-gradient(90deg, #6f6f6f, #f4f4f4 50%, #6f6f6f); }
  .swatch-black { background: var(--board); border: 1px solid var(--heading); }
  .legend-item { display: flex; align-items: center; margin-right: 46px; }

  .board-footer {
    position: absolute; left: 0; bottom: 0;
    width: 1200px; height: 44px; background: var(--footer);
  }
</style>
</head>
<body>
  <header>
    <h1 class="board-title">Dorvanel Wine Company<span class="divider"></span>Velisse</h1>
    <p class="board-subtitle">Sparkling Riesling Label Concept</p>
  </header>

  <p class="view-caption" style="left:76px">Front</p>
  <section class="label label-front" aria-label="Front label">
    <div class="label-band"><div class="label-rule"><div class="label-panel">
      <span class="brand-dot"></span>
      <h2 class="brand-name">Velisse</h2>
      <p class="varietal">Sparkling Riesling</p>
      <span class="spec spec-volume">750 ML</span>
      <span class="spec spec-abv">12% ALC BY VOL</span>
    </div></div></div>
  </section>

  <p class="view-caption" style="left:750px">Back</p>
  <section class="label label-back" aria-label="Back label">
    <div class="label-band"><div class="label-rule"><div class="label-panel">
      <span class="brand-dot"></span>
      <h2 class="brand-name">Velisse</h2>
      <p class="varietal">Sparkling Riesling</p>
      <span class="origin">Washington</span>
      <p class="website">www.dorvanelwineco.com</p>
      <p class="warning">Government Warning: (1) According to the Surgeon General, women should not drink alcoholic beverages during pregnancy because of the risk of birth defects. (2) Consumption of alcoholic beverages impairs your ability to drive a car or operate machinery, and may cause health problems.</p>
      <div class="back-specs"><span>CONTAINS SULFITES</span><span>12% ALC BY 750 ML VOL.</span></div>
      <p class="bottler">Vinted &amp; Bottled By Tidewater Cellars, Canas Ca for Dorvanel Wine Company, Los Angeles Ca.</p>
    </div></div></div>
  </section>

  <div class="legend">
    <div class="legend-item"><span class="swatch swatch-turquoise"></span>Turquoise</div>
    <div class="legend-item"><span class="swatch swatch-foil"></span>Silver Foil</div>
    <div class="legend-item"><span class="swatch swatch-black"></span>Black</div>
  </div>

  <footer class="board-footer"></footer>
</body>
</html>
```